Stationary, cards, memo form for 45 year old Investment Company
Brennor Equity Holdings Stationary
Simple
Dan Kessworth
President & CEO
517 Orchard Ridge Ave
Seattle, WA 98107-3815
Dan@Brennorcap.com
www.Brennorcap.com
Please design:
business card
Memo form
template that can be used from computer
The grey "L" in the circle may be used as a watermark.
This is a very low-key, sophisticated, company that provides investment for wealthy people and companies. Should be simple and elegant. Please error on the side of being more simple and straightforward...understated
This is the logo to use. Note grey "L" in circle may be used as a watermark.

```html
<!DOCTYPE html>
<html lang="en">
<head>
<meta charset="utf-8">
<title>Brennor Equity Holdings — Business Card</title>
<link rel="stylesheet" href="https://fonts.googleapis.com/css2?family=Cinzel:wght@400;600&display=swap">
<style>
  :root {
    --backdrop: #e9e7e3;
    --card: #ffffff;
    --teal: #13765f;
    --teal-light: #5fb39c;
    --charcoal: #35373a;
    --ink: #2c2d2f;
    --rule: #6b6d70;
    --shadow: rgba(0,0,0,0.18);
  }
  * { margin: 0; padding: 0; box-sizing: border-box; }
  html, body {
    width: 1200px; height: 914px; overflow: hidden;
    background: var(--backdrop);
  }
  .canvas {
    position: relative; width: 1200px; height: 914px;
    display: flex; align-items: center; justify-content: center;
  }
  .business-card {
    position: relative; width: 1000px; height: 572px;
    background: var(--card);
    box-shadow: 0 12px 40px var(--shadow);
    overflow: hidden;
    font-family: "Cinzel", serif;
    color: var(--ink);
  }
  .brand {
    position: absolute; top: 120px; left: 0; right: 0;
    display: flex; align-items: center; justify-content: center; gap: 28px;
  }
  .brand-dot {
    width: 92px; height: 92px; border-radius: 50%;
    background: var(--teal);
  }
  .brand-name {
    font-family: "Cinzel", serif; font-weight: 400;
    font-size: 40px; letter-spacing: 2px; color: var(--ink);
  }
  .details {
    position: absolute; top: 300px; left: 0; right: 0;
    display: flex; justify-content: center;
  }
  .identity {
    text-align: right; padding-right: 18px;
    font-size: 17px; line-height: 1.35;
  }
  .identity .person-name {
    color: var(--teal); font-size: 24px; font-weight: 600; letter-spacing: 0.5px;
  }
  .identity .person-title { font-size: 15px; margin-bottom: 18px; }
  .divider { width: 1.5px; background: var(--rule); }
  .contact-list {
    list-style: none; padding-left: 12px;
    font-size: 15px; line-height: 1.55;
  }
  .contact-list li { display: flex; align-items: center; gap: 8px; }
  .contact-icon { width: 15px; height: 15px; flex: none; }
  .footer-band { position: absolute; left: 0; bottom: 0; width: 1000px; height: 70px; }
</style>
</head>
<body>
<div class="canvas">
  <div class="business-card">
    <div class="brand">
      <div class="brand-dot"></div>
      <div class="brand-name">Brennor Equity Holdings</div>
    </div>

    <div class="details">
      <div class="identity">
        <div class="person-name">Dan Kessworth</div>
        <div class="person-title">President &amp; CEO</div>
        <div>517 Orchard Ridge Ave</div>
        <div>Seattle, WA 98107-3815</div>
      </div>
      <div class="divider"></div>
      <ul class="contact-list">
        <li><svg class="contact-icon" viewBox="0 0 16 16"><circle cx="8" cy="8" r="8" fill="var(--teal)"/><path d="M5 4.5l1.6-.4 1 2.2-1 .8a6 6 0 0 0 2.3 2.3l.8-1 2.2 1-.4 1.6c-3.5.2-6.7-3-6.5-6.5z" fill="#fff"/></svg>206-555-0148</li>
        <li><svg class="contact-icon" viewBox="0 0 16 16"><circle cx="8" cy="8" r="8" fill="var(--teal)"/><rect x="5.5" y="3.5" width="5" height="9" rx="1" fill="#fff"/></svg>206-555-0173</li>
        <li><svg class="contact-icon" viewBox="0 0 16 16"><circle cx="8" cy="8" r="8" fill="var(--teal)"/><rect x="4" y="6" width="8" height="5" fill="#fff"/><rect x="5.5" y="3.5" width="5" height="2.5" fill="#fff"/></svg>206-555-0192</li>
        <li><svg class="contact-icon" viewBox="0 0 16 16"><circle cx="8" cy="8" r="8" fill="var(--teal)"/><rect x="3.5" y="5" width="9" height="6" fill="#fff"/><path d="M3.5 5L8 8.5 12.5 5" stroke="var(--teal)" fill="none"/></svg>Dan@Brennorcap.com</li>
        <li><svg class="contact-icon" viewBox="0 0 16 16"><circle cx="8" cy="8" r="8" fill="var(--teal)"/><circle cx="8" cy="8" r="4.5" stroke="#fff" fill="none"/><path d="M3.5 8h9M8 3.5v9" stroke="#fff"/></svg>www.Brennorcap.com</li>
      </ul>
    </div>

    <svg class="footer-band" viewBox="0 0 1000 70" preserveAspectRatio="none">
      <defs>
        <linearGradient id="tealFade" x1="0" y1="0" x2="0" y2="1">
          <stop offset="0" stop-color="var(--teal-light)"/>
          <stop offset="0.45" stop-color="var(--teal)"/>
        </linearGradient>
      </defs>
      <polygon points="0,10 560,10 600,70 0,70" fill="url(#tealFade)"/>
      <polygon points="560,30 1000,30 1000,70 588,70" fill="var(--charcoal)"/>
    </svg>
  </div>
</div>
</body>
</html>
```